Supplement Company Needs a Protein Powder Pouch Design

We are looking for a modern and fresh design for our 500g pouches of protein powder as our current design is not eye catching or exciting enough.

This new design will be printed on both sides of a 178mm x 280mm x 101mm pouch.

We have 4 flavours. These are Banana Ice Cream, Chocolate Deluxe, Strawberries & Cream and Vanilla Ice Cream.

Industry/Entity Type

Supplement

Requirements
Must have
• Attractive and eye catching front and space for all the nutritional information and ingredients on the back.

Must clearly state 'food supplement' somewhere on the front of the pouch.
Nice to have
• Our logo is attached.
Should not have
• No health claims as these are not allowed in the UK

```html
<!DOCTYPE html>
<html lang="en">
<head>
<meta charset="utf-8">
<title>Quillo Supplements – Protein Powder Range</title>
<link href="https://fonts.googleapis.com/css2?family=Oswald:wght@300;400;600&display=swap" rel="stylesheet">
<style>
  :root {
    --page: #ffffff;
    --pouch: #111111;
    --pouch-edge: #1d1d1d;
    --text-light: #e9e9e9;
    --cream: #f4f1ea;
    --vanilla: #f1dcb0;
    --vanilla-tone: #b98553;
    --strawberry: #d3263f;
    --strawberry-tone: #c8303c;
    --banana: #f2bd1c;
    --banana-tone: #e8c93a;
    --chocolate: #5b2f23;
    --chocolate-tone: #4a241b;
  }
  * { box-sizing: border-box; margin: 0; padding: 0; }
  html, body { width: 1200px; height: 1000px; overflow: hidden; background: var(--page); }
  body { font-family: "Oswald", "Arial Narrow", sans-serif; }

  .range {
    position: absolute;
    top: 255px; left: 75px;
    display: flex; gap: 30px;
  }

  .pouch {
    position: relative;
    width: 240px; height: 470px;
    background: linear-gradient(90deg, var(--pouch-edge), var(--pouch) 20%, var(--pouch) 80%, var(--pouch-edge));
    border-radius: 16px 16px 10px 10px;
    color: var(--text-light);
    overflow: hidden;
  }
  .pouch--vanilla { --accent: var(--vanilla); --accent-ink: #7a5a2a; --tone: var(--vanilla-tone); --category: var(--vanilla); }
  .pouch--strawberry { --accent: var(--strawberry); --accent-ink: #ffffff; --tone: var(--strawberry-tone); --category: var(--strawberry); }
  .pouch--banana { --accent: var(--banana); --accent-ink: #ffffff; --tone: var(--banana-tone); --category: var(--banana); }
  .pouch--chocolate { --accent: var(--chocolate); --accent-ink: #ffffff; --tone: var(--chocolate-tone); --category: #6e4033; }

  .pouch__zip {
    position: absolute; top: 54px; left: 0; right: 0;
    height: 2px; background: #2a2a2a;
  }

  .brand-tab {
    position: absolute; top: 0; left: 50%;
    transform: translateX(-50%);
    width: 104px; height: 52px;
    background: var(--accent);
    border-radius: 0 0 6px 6px;
    display: flex; align-items: center; justify-content: center;
  }
  .brand-tab__name {
    font-weight: 600; font-size: 21px; letter-spacing: 0.5px;
    color: var(--accent-ink);
  }

  .pouch__label {
    position: absolute; top: 86px; left: 0; right: 0;
    text-align: center;
  }
  .pouch__category {
    font-weight: 300; font-size: 15px; letter-spacing: 0.5px;
    color: var(--category);
  }
  .pouch__title {
    margin-top: 4px;
    font-weight: 300; font-size: 56px; line-height: 1.0;
    letter-spacing: 1px;
  }

  .pouch__art {
    position: absolute; top: 240px; left: 14px; right: 14px;
    height: 190px;
    border-radius: 40px 40px 90px 90px;
    background: linear-gradient(170deg, var(--tone) 0%, var(--tone) 30%, var(--cream) 75%);
    opacity: 0.9;
  }

  .flavour-band {
    position: absolute; top: 392px; left: 10px; right: 22px;
    height: 30px;
    background: var(--accent);
    border-radius: 0 15px 15px 0;
    display: flex; align-items: center; justify-content: center;
    font-weight: 400; font-size: 14px; letter-spacing: 0.3px;
    color: var(--accent-ink);
    text-transform: uppercase;
  }

  .pouch__weight {
    position: absolute; bottom: 26px; right: 22px;
    font-weight: 300; font-size: 12px; color: var(--text-light);
  }
</style>
</head>
<body>
  <main class="range">
    <article class="pouch pouch--vanilla">
      <div class="brand-tab"><span class="brand-tab__name">QUILLO</span></div>
      <div class="pouch__zip"></div>
      <div class="pouch__label">
        <p class="pouch__category">FOOD SUPPLEMENT</p>
        <h2 class="pouch__title">PROTEIN<br>POWDER</h2>
      </div>
      <div class="pouch__art" role="img" aria-label="Photograph of cinnamon sticks, vanilla blossoms and a splash of cream"></div>
      <p class="flavour-band">Vanilla Icecream</p>
      <p class="pouch__weight">500 g</p>
    </article>

    <article class="pouch pouch--strawberry">
      <div class="brand-tab"><span class="brand-tab__name">QUILLO</span></div>
      <div class="pouch__zip"></div>
      <div class="pouch__label">
        <p class="pouch__category">FOOD SUPPLEMENT</p>
        <h2 class="pouch__title">PROTEIN<br>POWDER</h2>
      </div>
      <div class="pouch__art" role="img" aria-label="Photograph of fresh strawberries falling into a swirl of cream"></div>
      <p class="flavour-band">Strawberries &amp; Cream</p>
      <p class="pouch__weight">500 g</p>
    </article>

    <article class="pouch pouch--banana">
      <div class="brand-tab"><span class="brand-tab__name">QUILLO</span></div>
      <div class="pouch__zip"></div>
      <div class="pouch__label">
        <p class="pouch__category">FOOD SUPPLEMENT</p>
        <h2 class="pouch__title">PROTEIN<br>POWDER</h2>
      </div>
      <div class="pouch__art" role="img" aria-label="Photograph of bananas and banana slices over a swirl of cream"></div>
      <p class="flavour-band">Banana Icecream</p>
      <p class="pouch__weight">500 g</p>
    </article>

    <article class="pouch pouch--chocolate">
      <div class="brand-tab"><span class="brand-tab__name">QUILLO</span></div>
      <div class="pouch__zip"></div>
      <div class="pouch__label">
        <p class="pouch__category">FOOD SUPPLEMENT</p>
        <h2 class="pouch__title">PROTEIN<br>POWDER</h2>
      </div>
      <div class="pouch__art" role="img" aria-label="Photograph of chocolate pieces over a swirl of cream"></div>
      <p class="flavour-band">Chocolate Deluxe</p>
      <p class="pouch__weight">500 g</p>
    </article>
  </main>
</body>
</html>
```